Conservative, Modern and Sharp Builder Business card

Hi there,
We would like to update our existing business card.
I have attached photos of existing business card, logo and van sign.

I would like the business card to also list what we do :
Renovation • New Build • Alteration
Extension • Bathroom • Maintenance.(Seperated by dots)

Contact number : 021 0483 0752
(With that exact spacing)

Ideally when people looking from about 2-3 metres, they know that it is a builder’s business card

Open to suggestions on fonts, layout, style of business card

PLEASE ONLY SUBMIT YOUR BEST OR MAX 3 DESIGNS FOR EACH DESIGNER

Thanks

Industry/Entity Type

Construction. Renovation

Contact Information for Business Card

Details should be the same as the existing card. And addition of what we do.

Requirements
Should not have
• The new business card must not have the same layout as our existing one. Thanks

```html
<!DOCTYPE html>
<html lang="en">
<head>
<meta charset="utf-8">
<title>KestrelBuild Business Card</title>
<link href="https://fonts.googleapis.com/css2?family=Source+Sans+3:wght@400;600;700&display=swap" rel="stylesheet">
<style>
  :root {
    --backdrop: #9a9ca1;
    --ink: #000000;
    --paper: #ffffff;
    --rule: #1a1a1a;
  }
  html, body {
    margin: 0;
    padding: 0;
    width: 988px;
    height: 1200px;
    overflow: hidden;
    background: var(--backdrop);
    font-family: "Source Sans 3", sans-serif;
  }
  .canvas { position: relative; width: 988px; height: 1200px; }
  .card { position: absolute; border-radius: 32px; overflow: hidden; }
  .card--front { left: 65px; top: 94px; width: 840px; height: 476px; background: var(--ink); color: var(--paper); }
  .card--back { left: 74px; top: 627px; width: 840px; height: 476px; background: var(--paper); color: var(--ink); }
  .abs { position: absolute; line-height: 1; white-space: nowrap; }

  .brand-square { position: absolute; width: 46px; height: 46px; }
  .card--front .brand-square { left: 404px; top: 150px; background: var(--paper); }
  .card--back .brand-square { left: 206px; top: 200px; background: var(--ink); }

  .brand-name { font-weight: 700; letter-spacing: -1px; text-align: center; }
  .card--front .brand-name { left: 0; width: 840px; top: 241px; font-size: 88px; }
  .card--front .website { left: 0; width: 840px; top: 408px; font-size: 28px; font-weight: 600; letter-spacing: 0.42em; text-align: center; padding-left: 0.42em; box-sizing: border-box; }

  .card--back .brand-name { left: 0; width: 460px; top: 270px; font-size: 72px; }
  .divider { position: absolute; left: 439px; top: 75px; width: 1.5px; height: 306px; background: var(--rule); }
  .person-name { left: 488px; top: 76px; font-size: 35px; font-weight: 700; }
  .person-role { left: 489px; top: 118px; font-size: 17px; font-weight: 600; }
  .address { left: 489px; font-size: 16.5px; font-weight: 600; }
  .address--1 { top: 179px; }
  .address--2 { top: 214px; }
  .contact { left: 488px; display: flex; align-items: center; gap: 13px; font-size: 17px; font-weight: 600; }
  .contact svg { width: 22px; height: 22px; flex: none; }
  .contact--phone { top: 270px; }
  .contact--email { top: 315px; }
  .contact--social { top: 357px; }
  .services { left: 0; width: 840px; top: 436px; text-align: center; font-size: 19px; font-weight: 700; letter-spacing: 0.2px; }
</style>
</head>
<body>
<div class="canvas">
  <section class="card card--front">
    <div class="brand-square"></div>
    <div class="abs brand-name">KestrelBuild</div>
    <div class="abs website">www.kestrelbuild.nz</div>
  </section>

  <section class="card card--back">
    <div class="brand-square"></div>
    <div class="abs brand-name">KestrelBuild</div>
    <div class="divider"></div>
    <div class="abs person-name">Daniel Marsh</div>
    <div class="abs person-role">RESIDENTIAL BUILDER</div>
    <div class="abs address address--1">42 Harbourview Lane, Eastbrook,</div>
    <div class="abs address address--2">Northvale 5020, NZ</div>
    <div class="abs contact contact--phone">
      <svg viewBox="0 0 24 24" aria-hidden="true"><path d="M6.6 2.5l3 3.4-1.8 2.4c1.2 2.6 3.3 4.7 5.9 5.9l2.4-1.8 3.4 3-1.6 3.4C10.4 19.5 4.5 13.6 3.2 4.1z" fill="#000"/><path d="M14 3.5a6.5 6.5 0 0 1 6.5 6.5M14 6.5a3.5 3.5 0 0 1 3.5 3.5" stroke="#000" stroke-width="1.6" fill="none"/></svg>
      <span>021 0483 0752</span>
    </div>
    <div class="abs contact contact--email">
      <svg viewBox="0 0 24 24" aria-hidden="true"><rect x="2" y="5" width="20" height="14" fill="#000"/><path d="M3 6l9 7 9-7M3 18l7-6M21 18l-7-6" stroke="#fff" stroke-width="1.4" fill="none"/></svg>
      <span>kestrelbuild@mailbox.com</span>
    </div>
    <div class="abs contact contact--social">
      <svg viewBox="0 0 24 24" aria-hidden="true"><circle cx="12" cy="12" r="9.5" stroke="#000" stroke-width="2" fill="none"/></svg>
      <span>kestrelbuild.nz</span>
    </div>
    <div class="abs services">RENOVATION • NEW BUILD • ALTERATION • EXTENSION • BATHROOM • MAINTENANCE</div>
  </section>
</div>
</body>
</html>
```